website for Vindoralis.de

In Naturheilzentrum VINDORALIS, the medical team using the Advanced Laboratory examines the health status of patients and each patient is treated with special care in Germany. Multi language.
The design must show mix of modern medical service.
pages :
1. Home
2. Philosophie
3.Diagnose
4. Therapie
5. Kontakt
6.über uns
7. Zentrum ( Bilder )
8.Unser Ergebnisse
9. Anfahrt

Target Market(s)

International

Industry/Entity Type

Hospital

Font styles to use
Decorative

Colors
0455a3

Requirements
Must have
• The design must show mix of modern medical service.
• Advanced Laboratory abilities.
Nice to have
• Medical Theme

```html
<!DOCTYPE html>
<html lang="de">
<head>
<meta charset="utf-8">
<title>Vindoralis.de</title>
<link href="https://fonts.googleapis.com/css2?family=Lato:wght@400;700;900&family=Cinzel:wght@400&display=swap" rel="stylesheet">
<style>
:root{
  --brand:#0455a3;
  --navy:#0a3f9a;
  --deep:#0b2f84;
  --red:#e02a3a;
  --ink:#333;
  --panel:#d9d9d9;
  --white:#fff;
  --green:#6db33f;
  --soft:#c8d4ef;
}
*{margin:0;padding:0;box-sizing:border-box}
html,body{width:686px;height:1200px;overflow:hidden;background:var(--white)}
body{position:relative;font-family:'Lato',sans-serif;color:var(--ink)}
.abs{position:absolute}
.topnav{left:0;top:0;width:686px;height:34px;background:linear-gradient(90deg,#0a3a9a,var(--brand) 60%,#0a3a9a)}
.topnav ul{list-style:none;position:absolute;left:72px;top:0;height:34px;display:flex;gap:18px;align-items:center}
.topnav li{color:var(--white);font-size:8px;font-weight:700}
.search{left:598px;top:6px;width:24px;height:24px;background:var(--red);display:flex;align-items:center;justify-content:center}
.header{left:0;top:34px;width:686px;height:57px;background:var(--white)}
.logo{left:56px;top:50px;display:flex;align-items:center;gap:6px}
.logo .mark{width:12px;height:12px;background:var(--green)}
.logo span{font-size:17px;font-weight:700;color:var(--red);letter-spacing:.5px}
.emg-icon{left:490px;top:48px;width:24px;height:27px;background:var(--red);display:flex;align-items:center;justify-content:center}
.emg-label{left:520px;top:47px;color:var(--red);font-size:8.5px;font-weight:700}
.emg-phone{left:518px;top:58px;color:#111;font-size:17px}
.hero{left:0;top:91px;width:686px;height:298px;
  background:
    radial-gradient(ellipse 210px 170px at 560px 120px,rgba(235,240,248,.95),rgba(235,240,248,0) 70%),
    radial-gradient(ellipse 140px 120px at 420px 110px,rgba(150,170,200,.8),rgba(150,170,200,0) 70%),
    radial-gradient(ellipse 220px 160px at 290px 170px,rgba(40,120,230,.75),rgba(40,120,230,0) 70%),
    radial-gradient(ellipse 160px 110px at 640px 260px,rgba(210,222,240,.9),rgba(210,222,240,0) 70%),
    linear-gradient(100deg,#0a2a86 0%,#1450c0 38%,#3b7ad4 62%,#9fbbe0 100%)}
.hero-kicker{left:57px;top:187px;font-family:'Cinzel',serif;font-size:11.5px;color:var(--white);padding-bottom:4px;border-bottom:1px solid rgba(255,255,255,.6);width:245px}
.hero-title{left:57px;top:211px;font-size:16px;font-weight:900;color:var(--white);line-height:19px}
.btn-ghost{left:57px;top:258px;width:77px;height:20px;border:1.5px solid var(--white);color:var(--white);font-size:8.5px;font-weight:700;display:flex;align-items:center;justify-content:center}
.dots{left:61px;top:310px;display:flex;gap:8px}
.dots i{width:6px;height:6px;border-radius:50%;background:var(--white);display:block}
.dots i.off{background:none;border:1px solid var(--white)}
.card{top:347px;width:185px;height:231px;background:var(--white)}
.card h3{height:42px;display:flex;align-items:center;justify-content:center;color:var(--navy);font-size:13px;font-weight:900}
.card .photo{height:126px;position:relative}
.card .share{position:absolute;left:50%;bottom:0;transform:translateX(-50%);width:26px;height:13px;background:var(--white);clip-path:polygon(50% 0,100% 100%,0 100%)}
.card .arrow{position:absolute;left:50%;bottom:-1px;transform:translateX(-50%)}
.card p{font-size:6.4px;line-height:11.5px;text-align:center;padding:10px 14px 0;font-weight:400}
.card.active{background:var(--navy)}
.card.active h3,.card.active p{color:var(--white)}
.card.active .share{background:var(--navy)}
.card-shadow{top:578px;width:175px;height:6px;border-radius:50%;box-shadow:0 3px 5px rgba(0,0,0,.18)}
.sec-title{font-size:12px;font-weight:900;color:var(--navy)}
.para{font-size:6.6px;line-height:11.6px;color:var(--ink)}
.thumb{width:164px;height:103px}
.post-title{font-size:9.6px;font-weight:700;color:#333}
.post-meta{font-size:7px;font-weight:700;color:var(--brand)}
.acc{left:436px;width:194px;height:27px;background:var(--panel);display:flex;align-items:center;padding-left:6px;gap:9px;font-size:8.5px;color:#333}
.acc .dot{width:17px;height:17px;border-radius:50%;background:var(--white);display:flex;align-items:center;justify-content:center}
.acc.open{background:var(--navy);color:var(--white)}
.footer{left:0;top:930px;width:686px;height:230px;
  background:
    radial-gradient(ellipse 160px 120px at 300px 90px,rgba(40,90,200,.55),rgba(40,90,200,0) 70%),
    radial-gradient(ellipse 140px 110px at 580px 120px,rgba(40,90,200,.45),rgba(40,90,200,0) 70%),
    linear-gradient(120deg,#0c3a9c,#0a3490 50%,#0b3fa8)}
.f-title{font-size:10px;font-weight:700;color:var(--white)}
.f-text{font-size:7.5px;font-weight:700;color:var(--soft)}
.f-link{font-size:7.2px;font-weight:700;color:var(--soft);display:flex;align-items:center;gap:9px}
.f-link::before{content:"";width:0;height:0;border-left:4px solid var(--white);border-top:3px solid transparent;border-bottom:3px solid transparent}
.field{left:515px;width:113px;border-bottom:1px solid rgba(255,255,255,.4);font-size:7px;color:var(--soft);padding-bottom:4px}
.submit{left:520px;top:1113px;width:50px;height:16px;border:1.5px solid var(--white);color:var(--white);font-size:6.5px;font-weight:700;display:flex;align-items:center;justify-content:center}
.social{left:56px;top:1124px;display:flex;gap:13px}
.social i{width:12px;height:12px;border:1.5px solid var(--white);display:block}
.bottom{left:0;top:1160px;width:686px;height:40px;background:#eee;display:flex;align-items:center;justify-content:center;font-size:6.6px;color:#333}
</style>
</head>
<body>

<nav class="abs topnav">
  <ul>
    <li>Home</li><li>Philosophie</li><li>Diagnose</li><li>Therapie</li><li>Kontakt</li><li>über uns</li><li>Zentrum ( Bilder )</li><li>Unser Ergebnisse</li><li>Anfahrt</li>
  </ul>
</nav>
<div class="abs search">
  <svg width="9" height="9" viewBox="0 0 10 10"><circle cx="4" cy="4" r="3" fill="none" stroke="#fff" stroke-width="1.5"/><line x1="6.2" y1="6.2" x2="9" y2="9" stroke="#fff" stroke-width="1.5"/></svg>
</div>

<header class="abs header"></header>
<div class="abs logo"><i class="mark"></i><span>VINDORALIS</span></div>
<div class="abs emg-icon">
  <svg width="8" height="13" viewBox="0 0 8 13"><rect x=".7" y=".7" width="6.6" height="11.6" rx="1.2" fill="none" stroke="#fff" stroke-width="1.2"/><circle cx="4" cy="10.3" r=".8" fill="#fff"/></svg>
</div>
<div class="abs emg-label">CALL US FOR EMERGENCY</div>
<div class="abs emg-phone">1-800 240 3190</div>

<section class="abs hero" role="img" aria-label="Laboratory scientist looking through a microscope with a DNA helix overlay in blue tones"></section>
<div class="abs hero-kicker">We uses the Advanced Laboratory</div>
<h1 class="abs hero-title">EXAMINES THE HEALTH STATUS<br>OF PATIENTS</h1>
<div class="abs btn-ghost">LEARN MORE</div>
<div class="abs dots"><i></i><i class="off"></i><i></i><i></i></div>

<article class="abs card" style="left:56px">
  <h3>PHILOSOPHIE</h3>
  <div class="photo" role="img" aria-label="Black and white photo of a lab researcher holding a test tube" style="background:radial-gradient(ellipse 70px 60px at 120px 50px,#f2f2f2,rgba(242,242,242,0) 70%),radial-gradient(ellipse 60px 70px at 40px 90px,#5a5a5a,rgba(90,90,90,0) 70%),linear-gradient(135deg,#cfcfcf,#8a8a8a)"><span class="share"></span>
    <svg class="arrow" width="12" height="10" viewBox="0 0 12 10"><path d="M1 9C1 5 4 3 8 3V0l4 4-4 4V5C5 5 3 6 1 9z" fill="#0a3f9a"/></svg></div>
  <p>Lorem ipsum dolor sit amet, consectetur adipiscing elit, sed do eiusmod tempor incididunt ut labore et dolore magna aliqua.</p>
</article>
<article class="abs card active" style="left:251px">
  <h3>DIAGNOSE</h3>
  <div class="photo" role="img" aria-label="Doctors preparing a patient for an X-ray scan" style="background:radial-gradient(ellipse 60px 50px at 60px 40px,#6f8fc8,rgba(111,143,200,0) 70%),radial-gradient(ellipse 70px 40px at 90px 110px,#3a3a48,rgba(58,58,72,0) 70%),linear-gradient(135deg,#eceae6,#a8aab0)"><span class="share"></span>
    <svg class="arrow" width="12" height="10" viewBox="0 0 12 10"><path d="M1 9C1 5 4 3 8 3V0l4 4-4 4V5C5 5 3 6 1 9z" fill="#fff"/></svg></div>
  <p>Lorem ipsum dolor sit amet, consectetur adipiscing elit, sed do eiusmod tempor incididunt ut labore et dolore magna aliqua.</p>
</article>
<article class="abs card" style="left:446px">
  <h3>THERAPIE</h3>
  <div class="photo" role="img" aria-label="Black and white photo of a therapy session on an exercise ball" style="background:radial-gradient(ellipse 50px 70px at 60px 70px,#6e6e6e,rgba(110,110,110,0) 70%),radial-gradient(ellipse 50px 60px at 140px 50px,#f4f4f4,rgba(244,244,244,0) 70%),linear-gradient(135deg,#d8d8d8,#9a9a9a)"><span class="share"></span>
    <svg class="arrow" width="12" height="10" viewBox="0 0 12 10"><path d="M1 9C1 5 4 3 8 3V0l4 4-4 4V5C5 5 3 6 1 9z" fill="#0a3f9a"/></svg></div>
  <p>Lorem ipsum dolor sit amet, consectetur adipiscing elit, sed do eiusmod tempor incididunt ut labore et dolore magna aliqua.</p>
</article>
<div class="abs card-shadow" style="left:61px"></div>
<div class="abs card-shadow" style="left:451px"></div>

<h2 class="abs sec-title" style="left:57px;top:613px">ÜBER UNS</h2>
<p class="abs para" style="left:58px;top:636px;width:348px;text-align:justify">Lorem ipsum dolor sit amet, consectetur adipiscing elit, sed do eiusmod tempor incididunt ut labore et dolore magna aliqua. Ut enim ad minim veniam, quis nostrud exercitation ullamco laboris nisi ut aliquip ex ea commodo consequat. Duis aute irure dolor in reprehenderit in voluptate velit esse cillum dolore eu fugiat nulla pariatur. Excepteur sint occaecat cupidatat non proident, sunt in culpa qui officia deserunt mollit anim id est laborum</p>

<div class="abs thumb" style="left:58px;top:703px;background:radial-gradient(ellipse 50px 45px at 90px 55px,#d8b49a,rgba(216,180,154,0) 70%),radial-gradient(ellipse 60px 50px at 150px 60px,#e8eef2,rgba(232,238,242,0) 70%),linear-gradient(135deg,#39c0e0,#0f7fb4 60%,#0b5f92)" role="img" aria-label="Hand touching a digital DNA interface"></div>
<div class="abs thumb" style="left:242px;top:703px;background:radial-gradient(ellipse 40px 55px at 80px 70px,#ffffff,rgba(255,255,255,0) 70%),radial-gradient(ellipse 22px 24px at 80px 25px,#e8c9a8,rgba(232,201,168,0) 70%),linear-gradient(135deg,#f1f6fb,#bcd2e6)" role="img" aria-label="Smiling doctor holding a clipboard"></div>

<h4 class="abs post-title" style="left:56px;top:821px">LOREM IPSUM DOLOR SIT AMET,</h4>
<div class="abs post-meta" style="left:58px;top:838px">Jan 19, 2018 &nbsp;|&nbsp; Dr. Jon Doe</div>
<p class="abs para" style="left:58px;top:856px;width:160px;font-size:7.6px;line-height:14.6px">Sed ut perspiciatis unde omnis iste natus error sit voluptatem accusantium doloremque laudantium.</p>

<h4 class="abs post-title" style="left:243px;top:821px">FINIBUS BONORUM ET MALORUM</h4>
<div class="abs post-meta" style="left:243px;top:838px">Jan 19, 2018 &nbsp;|&nbsp; Dr. Jon Doe</div>
<p class="abs para" style="left:242px;top:856px;width:160px;font-size:7.6px;line-height:14.6px">Sed ut perspiciatis unde omnis iste natus error sit voluptatem accusantium doloremque laudantium.</p>

<h2 class="abs sec-title" style="left:436px;top:614px">UNSER ERGEBNISSE</h2>
<p class="abs para" style="left:436px;top:643px;width:194px;line-height:13.6px">Sed ut perspiciatis unde omnis iste natus error sit voluptatem accusantium doloremque laudantium.Sed ut perspiciatis unde omnis iste natus error sit voluptatem accusantium</p>

<div class="abs acc open" style="top:704px"><span class="dot"><svg width="6" height="7" viewBox="0 0 6 7"><path d="M0 0L6 3.5 0 7z" fill="#0a3f9a"/></svg></span>Heart Treatment</div>
<p class="abs para" style="left:436px;top:734px;width:194px;line-height:13.6px">Sed ut perspiciatis unde omnis iste natus error s.it voluptatem accusantium doloremque laudantium.Sed ut perspiciatis unde omnis iste natus error sit voluptatem accusantium doloremque laudantium.</p>
<div class="abs acc" style="top:805px"><span class="dot"><svg width="6" height="7" viewBox="0 0 6 7"><path d="M0 0L6 3.5 0 7z" fill="#0a3f9a"/></svg></span>Health status</div>
<div class="abs acc" style="top:835px"><span class="dot"><svg width="6" height="7" viewBox="0 0 6 7"><path d="M0 0L6 3.5 0 7z" fill="#0a3f9a"/></svg></span>Finibus Bonorum</div>
<div class="abs acc" style="top:866px"><span class="dot"><svg width="6" height="7" viewBox="0 0 6 7"><path d="M0 0L6 3.5 0 7z" fill="#0a3f9a"/></svg></span>Malorum</div>

<footer class="abs footer"></footer>
<h5 class="abs f-title" style="left:57px;top:959px">Kontakt</h5>
<svg class="abs" style="left:57px;top:1003px" width="20" height="14" viewBox="0 0 20 14"><rect x=".6" y=".6" width="18.8" height="12.8" fill="none" stroke="#c8d4ef"/><path d="M.6 .6L10 8 19.4.6" fill="none" stroke="#c8d4ef"/></svg>
<div class="abs f-text" style="left:98px;top:1007px">info@vindoralis.de</div>
<svg class="abs" style="left:58px;top:1032px" width="12" height="19" viewBox="0 0 12 19"><rect x=".6" y=".6" width="10.8" height="17.8" rx="1.5" fill="none" stroke="#c8d4ef"/><line x1="1" y1="15" x2="11" y2="15" stroke="#c8d4ef"/></svg>
<div class="abs f-text" style="left:96px;top:1038px">1-800 240 3191</div>
<svg class="abs" style="left:56px;top:1071px" width="20" height="20" viewBox="0 0 20 20"><path d="M10 1a5 5 0 015 5c0 4-5 9-5 9S5 10 5 6a5 5 0 015-5z" fill="none" stroke="#c8d4ef"/><circle cx="10" cy="6" r="1.8" fill="none" stroke="#c8d4ef"/><path d="M5 13L1 19h18l-4-6" fill="none" stroke="#c8d4ef"/></svg>
<div class="abs f-text" style="left:99px;top:1068px;line-height:11px">48, Lindenweg, Altstadt,<br>Musterland 104220</div>
<div class="abs social" aria-label="Social media links"><i></i><i></i><i></i><i></i><i></i></div>

<h5 class="abs f-title" style="left:230px;top:958px">Quick Links</h5>
<div class="abs f-link" style="left:238px;top:1002px">Home</div>
<div class="abs f-link" style="left:238px;top:1020px">über uns</div>
<div class="abs f-link" style="left:238px;top:1038px">Zentrum ( Bilder )</div>
<div class="abs f-link" style="left:238px;top:1057px">Unser Ergebnisse</div>
<div class="abs f-link" style="left:238px;top:1075px">Anfahrt</div>

<h5 class="abs f-title" style="left:363px;top:959px">Our Services</h5>
<div class="abs f-link" style="left:363px;top:1002px">Philosophie</div>
<div class="abs f-link" style="left:363px;top:1021px">Diagnose</div>
<div class="abs f-link" style="left:363px;top:1039px">Therapie</div>

<h5 class="abs f-title" style="left:515px;top:958px">Enquiry Form</h5>
<div class="abs field" style="top:999px">Name</div>
<div class="abs field" style="top:1027px">Phone</div>
<div class="abs field" style="top:1054px;height:47px">Message</div>
<div class="abs submit">SUBMIT</div>

<div class="abs bottom">Copyright © 2018 &nbsp;|&nbsp; www.vindoralis.de</div>

</body>
</html>
```